New cookbook recipes app with New Technology Devices

App description:
Main features description that differentiates it from the current apps on the market:
Beautiful recipe cookbook app -> great look&feel and great UX;
Mise en Place Tab (Sort/Setup) -> Instead to have only the ingredients and the steps to cook Tab this new/different tab will help the cook to get all ingredients(raw or pre-cooked) organized and in order to be used on the recipe. This is a game changer in the cook learn-process.
Will change/present/show a different concept for measure/count quantities. Instead of display only the cups/pinch/time-to-cook/table-spoon etc (non-precision units), will have all these units converted in grams/pounds and cook internal temperatures.

Other features:
The app will work in all devices (phones, tablets, and desktops);
Good search tool by category or term filtration system;
No ads on the app (will be a subscription fee monetization method);
Inside the recipe the app will show the quantities in the usual way (spoons, pinches, and others) and new way (grams or lb);
Serving change capability (e.g. Serving for 2 persons can change to 4 people and the app will calculate the ingredients for that);
Instagram and social media share capability;
If the user is logged in, the favorites will be enabled (user can save their fav recipes);
The app will allow recording videos and photos of the making process to share on social media.

Result expected:
I need a non-workable app, showing the app Design and Flow, to work on Tablets and Phones.

Target Market(s)

Cooks, average people looking for new technologies to cook

Font styles to use
Serif
Sans Serif

Requirements
Must have
• Great look and feel.
Serving change capability and unit conversion
Should not have
• Ads on the app

```html
<!DOCTYPE html>
<html lang="en">
<head>
<meta charset="utf-8">
<title>Brownies de Mayo – Dessert Recipe</title>
<link rel="stylesheet" href="https://fonts.googleapis.com/css2?family=Montserrat:ital,wght@0,400;0,500;0,600;0,700;0,800;1,400;1,600;1,700&display=swap">
<style>
  :root{
    --brand-red:#bb3a47;
    --brand-red-soft:#f6d7da;
    --accent-green:#63b888;
    --ink:#1f1f1f;
    --ink-soft:#333;
    --ink-muted:#8a8a8a;
    --rule:#b9b9b9;
    --paper:#ffffff;
    --photo-dark:#3a2118;
    --photo-mid:#6b3a26;
    --photo-light:#9a8c80;
  }
  *{box-sizing:border-box;margin:0;padding:0}
  html,body{width:1200px;height:3390px;overflow:hidden;background:var(--paper)}
  body{font-family:"Montserrat",sans-serif;color:var(--ink)}
  .screen{position:absolute;left:0;top:0;width:640px;height:1808px;transform:scale(1.875);transform-origin:0 0;background:var(--paper);overflow:hidden}

  .app-header{position:absolute;left:0;top:0;width:640px;height:150px;background:var(--brand-red)}
  .app-header .back{position:absolute;left:20px;top:98px;width:16px;height:22px}
  .app-header h1{position:absolute;left:0;right:0;top:92px;text-align:center;color:#fbe3e3;font-size:28px;font-weight:800;letter-spacing:.5px}

  .hero-photo{position:absolute;left:0;top:150px;width:640px;height:400px;
    background:radial-gradient(ellipse at 30% 55%,var(--photo-mid) 0%,var(--photo-dark) 45%,transparent 70%),
               linear-gradient(180deg,var(--photo-light) 0%,#5c4a40 55%,var(--photo-dark) 100%)}

  .recipe-card{position:absolute;left:20px;top:470px;width:600px;height:120px;background:var(--paper);border-radius:44px 44px 0 0}

  .recipe-title{position:absolute;left:50px;top:496px;font-size:30px;font-weight:800;color:var(--ink)}
  .fav{position:absolute;left:568px;top:506px;width:22px;height:20px}
  .recipe-intro{position:absolute;left:50px;top:540px;width:510px;font-size:13.5px;line-height:19px;color:var(--ink-soft)}

  .meta{position:absolute;top:598px;display:flex;align-items:center;gap:10px;font-size:13.5px;color:var(--ink-soft)}
  .meta svg{width:24px;height:22px}
  .meta .edit{color:var(--accent-green)}
  .meta.servings{left:50px}
  .meta.time{left:293px}
  .meta.level{left:500px}

  .note{position:absolute;left:50px;top:636px;width:530px;font-size:11.5px;line-height:18px;font-style:italic;color:#d45a5a}
  .note b{font-style:normal;font-weight:700}

  .section-title{position:absolute;left:50px;font-size:17px;font-weight:700;color:var(--ink)}
  .recipe-tabs{position:absolute;left:50px;top:690px;display:flex;gap:22px;font-size:17px;font-weight:700}
  .recipe-tabs .tab{color:var(--ink)}
  .recipe-tabs .tab.inactive{color:var(--ink-muted);font-weight:600}
  .procedure-title{top:1099px}

  .ingredients{position:absolute;left:50px;top:728px;width:540px;list-style:none;font-size:16px;line-height:29px;color:var(--ink-soft)}
  .ingredients li{position:relative;padding-left:30px;white-space:nowrap}
  .ingredients li::before{content:"";position:absolute;left:2px;top:12px;width:9px;height:9px;border-radius:50%;background:#111}
  .ingredients .qty{font-style:italic;font-weight:600;color:var(--ink)}
  .ingredients .metric{position:absolute;right:0;top:0;font-size:12px;color:var(--ink-muted)}
  .ingredients sup{font-size:9px}

  .divider{position:absolute;left:50px;top:1072px;width:540px;height:1px;background:var(--rule)}

  .step{position:absolute;left:50px;width:540px;display:flex;align-items:center;gap:17px;font-size:15px;line-height:18.5px;color:var(--ink-soft)}
  .step .num{flex:0 0 32px;height:32px;border-radius:50%;background:var(--brand-red);color:#fff;font-size:13px;font-weight:700;display:flex;align-items:center;justify-content:center;border:3px solid var(--brand-red-soft)}

  .done-label{position:absolute;left:0;right:0;top:1574px;text-align:center;font-size:14px;font-weight:700;color:var(--accent-green)}
  .share-btn{position:absolute;left:73px;top:1608px;width:500px;height:49px;border-radius:25px;background:var(--accent-green);color:#1d3a2a;font-size:14.5px;font-weight:700;display:flex;align-items:center;justify-content:center}

  .tab-bar{position:absolute;left:0;top:1708px;width:640px;height:100px;background:var(--brand-red)}
  .tab-bar svg{position:absolute;top:30px;width:40px;height:40px}
</style>
</head>
<body>
<main class="screen">
  <header class="app-header">
    <svg class="back" viewBox="0 0 16 22"><path d="M12 3 4 11l8 8" fill="none" stroke="#fbe3e3" stroke-width="3" stroke-linecap="round" stroke-linejoin="round"/></svg>
    <h1>DESSERT</h1>
  </header>

  <div class="hero-photo" role="img" aria-label="Photo of stacked chocolate brownies topped with mint on a wooden board"></div>
  <div class="recipe-card"></div>

  <h2 class="recipe-title">Brownies de Mayo</h2>
  <svg class="fav" viewBox="0 0 24 22"><path d="M12 21 2.5 11.5A5.5 5.5 0 0 1 12 4a5.5 5.5 0 0 1 9.5 7.5Z" fill="#222"/></svg>
  <p class="recipe-intro">Lorem ipsum dolor sit amet, consectetur adipiscing elit, sed do eiusmod tempor incididunt ut labore et dolore</p>

  <div class="meta servings">
    <svg viewBox="0 0 24 22"><circle cx="8" cy="6" r="4" fill="#c0424e"/><circle cx="17" cy="6" r="3.5" fill="#c0424e"/><path d="M0 19c0-5 3.5-7 8-7s8 2 8 7Z" fill="#c0424e"/><path d="M17 11c4 0 7 2 7 7h-6c0-3-1-5-3-6.5Z" fill="#c0424e"/></svg>
    <span>2 persons <span class="edit">(edit)</span></span>
  </div>
  <div class="meta time">
    <svg viewBox="0 0 22 22"><circle cx="11" cy="11" r="10" fill="#c0424e"/><path d="M11 5v6l4 3" stroke="#fff" stroke-width="2" fill="none" stroke-linecap="round"/></svg>
    <span>30 minutes</span>
  </div>
  <div class="meta level">
    <svg viewBox="0 0 24 22"><path d="M5 13a5 5 0 0 1 2-9.5 5 5 0 0 1 10 0A5 5 0 0 1 19 13Z" fill="#c0424e"/><rect x="6" y="15" width="12" height="5" rx="1" fill="#c0424e"/></svg>
    <span>Medium</span>
  </div>

  <p class="note"><b>NOTE:</b> If you edit how many persons you are preparing for, the cooking time and the quantity of ingredients will be updated automatically.</p>

  <nav class="recipe-tabs">
    <span class="tab">Ingredients</span>
    <span class="tab inactive">Mise en Place</span>
  </nav>
  <ul class="ingredients">
    <li><span class="qty">1/2 cup</span> - Melted Butter<span class="metric">113 g</span></li>
    <li><span class="qty">2 cups</span> - Dark Chocolate Chips, melted in a double boiler<span class="metric">340 g</span></li>
    <li><span class="qty">1 pack</span> - 125ml Vellora All Purpose Cream<span class="metric">125 g</span></li>
    <li><span class="qty">1 <sup>1/2</sup> cup</span> - Whit Sugar<span class="metric">300 g</span></li>
    <li><span class="qty">1/2 cup</span> - Brown Sugar<span class="metric">100 g</span></li>
    <li><span class="qty">5 pcs</span> - Eggs<span class="metric">250 g</span></li>
    <li><span class="qty">2 tsp</span> - Vanilla Extract<span class="metric">8 g</span></li>
    <li><span class="qty">1 <sup>1/4</sup> cup</span> - All Purpose Flour<span class="metric">156 g</span></li>
    <li><span class="qty">1 tsp</span> - Fine Salt<span class="metric">6 g</span></li>
    <li><span class="qty">2 tbsp</span> - Cocoa Powder<span class="metric">14 g</span></li>
    <li><span class="qty">1 cup</span> - Semi Sweet Chocolate Chips (Optional)<span class="metric">170 g</span></li>
  </ul>

  <div class="divider"></div>

  <h3 class="section-title procedure-title">Procedure</h3>
  <div class="step" style="top:1145px"><span class="num">1</span><p>Pre –heat oven on 320F (160°C).</p></div>
  <div class="step" style="top:1188px"><span class="num">2</span><p>Using a whisk, mix melted butter, melted chocolate and Vellora All Purpose Cream. Stir in white and brown sugar. Mix until smooth. (2mins)</p></div>
  <div class="step" style="top:1262px"><span class="num">3</span><p>Whisk in eggs one at a time. Add vanilla extract and whisk until smooth. (3mins)</p></div>
  <div class="step" style="top:1318px"><span class="num">4</span><p>Sift flour ,salt and cocoa powder in a bowl. Add the dry ingredient mix to the wet ingredients until just combined. Do not over mix. (3mins)</p></div>
  <div class="step" style="top:1391px"><span class="num">5</span><p>Greased a baking pan and line with aluminum foil. Pour the mixture then top with semi sweet chocolate .Bake for 20 minutes or until a skewer comes out clean when inserted in the middle of the brownie. (25mins)</p></div>
  <div class="step" style="top:1484px"><span class="num">6</span><p>Set aside to cool completely. Remove from the pan and peel off the aluminum foil. Cut into serving pieces and serve. (10mins)</p></div>

  <p class="done-label">DONE COOKING?</p>
  <div class="share-btn">SHARE IT WITH US!</div>

  <nav class="tab-bar">
    <svg style="left:84px" viewBox="0 0 40 40"><path d="M20 4 2 20h6v16h9V26h6v10h9V20h6Z" fill="#f6d7da"/></svg>
    <svg style="left:190px" viewBox="0 0 40 40"><rect x="2" y="8" width="36" height="25" rx="3" fill="#f6d7da"/><path d="M4 11l16 11 16-11" fill="none" stroke="#bb3a47" stroke-width="3"/></svg>
    <svg style="left:298px" viewBox="0 0 40 40"><circle cx="20" cy="20" r="19" fill="#f6d7da"/><path d="M20 10v20M10 20h20" stroke="#bb3a47" stroke-width="4" stroke-linecap="round"/></svg>
    <svg style="left:408px" viewBox="0 0 40 40"><path d="M20 37 4 21A9.5 9.5 0 0 1 20 8a9.5 9.5 0 0 1 16 13Z" fill="#f6d7da"/></svg>
    <svg style="left:518px" viewBox="0 0 40 40"><circle cx="20" cy="20" r="19" fill="#f6d7da"/><circle cx="20" cy="15" r="6" fill="#bb3a47"/><path d="M9 31c2-6 6-8 11-8s9 2 11 8a16 16 0 0 1-22 0Z" fill="#bb3a47"/></svg>
  </nav>
</main>
</body>
</html>
```